Premium wine label refresh for Birch &Vale wines

Our Birch & Vale label is dated. We're looking for a contemporary refresh that will stand out on the shelf, make a strong quality statement and a more contemporary look. Feel free to take a completely fresh approach but the label should connect with the brand story. Birch & Vale refers to my convict ancestry and is a tribute to humble beginnings. Where we finish is not necessarily where we start.

Target Market(s)

Aspirational, educated wine drinkers 30-55

Industry/Entity Type

Wine

Font styles to use
Sans Serif

Requirements
Must have
• Shelf presence, premium feel, connection to the existing label
Nice to have
• Print quality cues like embossing, foil etc.
Should not have
• Fun look and feel.

```html
<!DOCTYPE html>
<html lang="en">
<head>
<meta charset="utf-8">
<title>Birch &amp; Vale – Single Vineyards Label</title>
<link rel="stylesheet" href="https://fonts.googleapis.com/css2?family=Barlow+Semi+Condensed:wght@400;500;600&family=Barlow:wght@600&display=swap">
<style>
  :root {
    --backdrop: #e8e8e8;
    --label-navy: #1c2769;
    --cream: #f2ecdf;
    --silver: #c9cad3;
    --vignette-top: #27337a;
    --vignette-bottom: #1a2462;
  }
  * { margin: 0; padding: 0; box-sizing: border-box; }
  html, body {
    width: 1200px;
    height: 1200px;
    overflow: hidden;
    background: var(--backdrop);
  }
  .canvas {
    position: relative;
    width: 1200px;
    height: 1200px;
  }
  .wine-label {
    position: absolute;
    left: 0;
    top: 159px;
    width: 1200px;
    height: 882px;
    background: var(--label-navy);
    color: var(--cream);
    font-family: "Barlow Semi Condensed", "Arial Narrow", sans-serif;
    text-align: center;
  }
  .brand-name {
    position: absolute;
    left: 0;
    right: 0;
    top: 10px;
    font-weight: 500;
    font-size: 158px;
    line-height: 1;
    letter-spacing: 2px;
  }
  .range-name {
    position: absolute;
    left: 0;
    right: 0;
    top: 176px;
    font-weight: 400;
    font-size: 44px;
    line-height: 1;
  }
  .region-box {
    position: absolute;
    left: 425px;
    top: 236px;
    width: 351px;
    height: 55px;
    border: 1.5px solid var(--silver);
    font-weight: 400;
    font-size: 42px;
    line-height: 52px;
  }
  .vineyard-vignette {
    position: absolute;
    left: 403px;
    top: 307px;
    width: 396px;
    height: 396px;
  }
  .wine-name {
    position: absolute;
    left: 0;
    right: 0;
    top: 728px;
    font-family: "Barlow", "Arial", sans-serif;
    font-weight: 600;
    font-size: 100px;
    line-height: 1;
    letter-spacing: 3px;
  }
  .vintage-varietal {
    position: absolute;
    left: 0;
    right: 0;
    top: 831px;
    font-weight: 400;
    font-size: 45px;
    line-height: 1;
  }
</style>
</head>
<body>
  <main class="canvas">
    <section class="wine-label">
      <h1 class="brand-name">BIRCH &amp; VALE</h1>
      <p class="range-name">SINGLE WINEYARDS</p>
      <p class="region-box">HILLTOPS</p>
      <svg class="vineyard-vignette" viewBox="0 0 396 396" role="img" aria-label="Circular line illustration of rolling vineyard hills beneath a mountain ridge and setting sun">
        <defs>
          <linearGradient id="vignetteFill" x1="0" y1="0" x2="0" y2="1">
            <stop offset="0" stop-color="var(--vignette-top)"/>
            <stop offset="1" stop-color="var(--vignette-bottom)"/>
          </linearGradient>
        </defs>
        <circle cx="198" cy="198" r="196" fill="url(#vignetteFill)" stroke="var(--silver)" stroke-width="1.5"/>
      </svg>
      <h2 class="wine-name">TARROW</h2>
      <p class="vintage-varietal">2022 CABERNET SAUVIGNON</p>
    </section>
  </main>
</body>
</html>
```